Business Card for Jewelry Business

We need a new namecard design for a jewelry company based in Bangkok, Thailand. We have a new website recently and want the new namecard to reflect our new modern image. I have uploaded our old namecard to show you the information that needs to be on the namecard. Pls check our website www.qelburn.com for the new color scheme to help design the new namecard.

```html
<!DOCTYPE html>
<html lang="en">
<head>
<meta charset="utf-8">
<title>Qelburn Makers – Business Card</title>
<link href="https://fonts.googleapis.com/css2?family=Cormorant+Garamond:wght@500&family=Montserrat:wght@400;700&display=swap" rel="stylesheet">
<style>
  :root {
    --teal: #5cbfc9;
    --teal-line: #8fd3da;
    --beige: #e9e2da;
    --circle-line: #ddd3c8;
    --ink: #2b2b2b;
    --white: #ffffff;
    --backdrop: #2e2e2e;
  }
  * { margin: 0; padding: 0; box-sizing: border-box; }
  html, body { width: 1200px; height: 1186px; overflow: hidden; }
  body { background: var(--backdrop); position: relative; font-family: "Montserrat", sans-serif; }

  .card {
    position: absolute; left: 160px; width: 880px; height: 500px;
    border-radius: 34px; overflow: hidden;
    box-shadow: 0 10px 30px rgba(0,0,0,.45);
  }
  .card--front { top: 70px; background: var(--teal); }
  .card--back { top: 616px; background: var(--white); }

  /* front */
  .brand-front {
    position: absolute; left: 250px; top: 170px;
    display: flex; align-items: center; gap: 22px; color: var(--white);
  }
  .brand-front__dot { width: 70px; height: 70px; border-radius: 50%; border: 3px solid var(--white); }
  .brand-front__name {
    font-family: "Cormorant Garamond", serif; font-weight: 500;
    font-size: 78px; letter-spacing: 4px; line-height: 1;
  }
  .brand-front__sub {
    font-family: "Cormorant Garamond", serif; font-weight: 500;
    font-size: 22px; letter-spacing: 3px; margin-top: 8px; margin-left: 90px;
  }

  /* back */
  .band--beige { position: absolute; left: 40px; top: 0; width: 300px; height: 250px; background: var(--beige); }
  .band--teal { position: absolute; left: 0; top: 250px; width: 400px; height: 250px; background: var(--teal); }
  .emblem {
    position: absolute; left: 70px; top: 100px; width: 300px; height: 300px;
    border-radius: 50%; background: var(--white);
    display: flex; align-items: center; justify-content: center;
  }
  .emblem__ring {
    width: 250px; height: 250px; border-radius: 50%; border: 3px solid var(--circle-line);
    display: flex; align-items: center; justify-content: center;
    font-family: "Cormorant Garamond", serif; font-weight: 500; font-size: 34px;
    letter-spacing: 3px; color: var(--teal);
  }

  .details { position: absolute; left: 450px; top: 48px; width: 400px; color: var(--ink); }
  .details__name { font-weight: 700; font-size: 34px; color: var(--teal); line-height: 1.1; }
  .details__role { font-size: 17px; margin-top: 2px; }
  .rule { height: 2px; background: var(--teal-line); margin: 12px 0; }
  .details__company { font-weight: 700; font-size: 17px; color: var(--teal); }
  .details__address { font-size: 17px; line-height: 1.3; }
  .contacts { list-style: none; margin-top: 14px; }
  .contacts li { display: flex; align-items: center; gap: 14px; font-size: 17px; line-height: 1.55; }
  .contacts svg { width: 16px; height: 16px; flex: none; fill: var(--teal); }
</style>
</head>
<body>

<section class="card card--front">
  <div class="brand-front">
    <span class="brand-front__dot"></span>
    <div>
      <div class="brand-front__name">QELBURN</div>
      <div class="brand-front__sub">MAKERS</div>
    </div>
  </div>
</section>

<section class="card card--back">
  <div class="band--beige"></div>
  <div class="band--teal"></div>
  <div class="emblem"><div class="emblem__ring">QELBURN</div></div>

  <div class="details">
    <h1 class="details__name">Nira Sompong</h1>
    <p class="details__role">Sales &amp; Product Development Manager</p>
    <div class="rule"></div>
    <p class="details__company">Qelburn Makers Co. Ltd</p>
    <p class="details__address">218 Moo 7, Export Processing Zone 2<br>Rim Klong Industrial Estate,<br>Bangkok, 10990 thailand</p>
    <div class="rule"></div>
    <ul class="contacts">
      <li><svg viewBox="0 0 16 16"><path d="M3 1l3 3-2 2c1 2 3 4 5 5l2-2 3 3-2 3C6 15 1 10 0 3z"/></svg>662-555-0141</li>
      <li><svg viewBox="0 0 16 16"><rect x="2" y="5" width="12" height="9" rx="1"/><rect x="4" y="1" width="8" height="4"/></svg>662-555-0178</li>
      <li><svg viewBox="0 0 16 16"><path d="M1 3h14v10H1z M1 3l7 6 7-6" /></svg>nira@qelburn.com</li>
      <li><svg viewBox="0 0 16 16"><path d="M1 3h14v10H1z M1 3l7 6 7-6" /></svg>info@qelburn.com</li>
      <li><svg viewBox="0 0 16 16"><circle cx="8" cy="8" r="7"/></svg>www.qelburn.com</li>
      <li><svg viewBox="0 0 16 16"><circle cx="8" cy="8" r="7"/></svg>@qelburn makers</li>
      <li><svg viewBox="0 0 16 16"><circle cx="8" cy="8" r="7"/></svg>@qelburn mfr</li>
    </ul>
  </div>
</section>

</body>
</html>
```